Cardiology practice business card

We need a business card for our cardiology practice "Bellmoor Cardiology". We have a new logo, attached below. We like the colours in the logo - red and charcoal. The front of the business card will need to have the doctors name, address, phone number and email. The back will need to have space to write 2 appointment dates and times.

```html
<!DOCTYPE html>
<html lang="en">
<head>
<meta charset="utf-8">
<title>Bellmoor Cardiology – Business Card</title>
<link href="https://fonts.googleapis.com/css2?family=Poppins:wght@400;500;600;700&display=swap" rel="stylesheet">
<style>
  :root {
    --red: #e8202a;
    --charcoal: #4d4e52;
    --ink: #1f1f21;
    --rule: #b9b9b9;
    --paper: #ffffff;
    --backdrop: #d3d7d7;
  }
  * { box-sizing: border-box; margin: 0; padding: 0; }
  html, body { width: 1200px; height: 960px; overflow: hidden; }
  body {
    background: var(--backdrop);
    font-family: "Poppins", sans-serif;
    color: var(--ink);
    position: relative;
  }
  .card {
    position: absolute;
    top: 105px;
    width: 428px;
    height: 748px;
    background: var(--paper);
    border-radius: 26px;
    box-shadow: -3px 3px 0 var(--red);
    overflow: hidden;
  }
  .card--back { left: 147px; }
  .card--front { left: 636px; }

  /* ---------- Back: appointment side (content set sideways) ---------- */
  .back-layout {
    position: absolute;
    left: 0; top: 0;
    width: 748px; height: 428px;
    transform-origin: top left;
    transform: translateY(748px) rotate(-90deg);
  }
  .back-brand {
    position: absolute;
    left: 296px; top: 34px;
    display: flex; align-items: center; gap: 8px;
    color: var(--red);
    font-weight: 600;
    font-size: 17px;
    line-height: 1.1;
    letter-spacing: 1px;
    text-transform: uppercase;
  }
  .brand-dot {
    width: 12px; height: 12px; border-radius: 50%;
    background: var(--red); flex: none;
  }
  .back-title {
    position: absolute;
    left: 283px; top: 104px;
    color: var(--red);
    font-size: 27px;
    font-weight: 500;
    line-height: 1;
  }
  .slot {
    position: absolute;
    left: 92px;
    width: 563px; height: 122px;
    border: 3px solid var(--accent);
    border-radius: 8px;
    background: var(--accent);
    display: flex; flex-direction: column;
  }
  .slot--first { top: 149px; --accent: var(--red); }
  .slot--second { top: 280px; --accent: var(--charcoal); }
  .slot__days {
    height: 35px;
    display: flex; align-items: center; justify-content: space-between;
    padding: 0 8px 0 8px;
    color: var(--paper);
    font-size: 18px;
    font-weight: 500;
  }
  .slot__days span { width: 76px; text-align: center; }
  .slot__fields {
    flex: 1;
    background: var(--paper);
    border-radius: 6px;
    padding: 6px 12px 0 8px;
    display: flex; flex-direction: column; justify-content: space-around;
  }
  .field-row {
    display: flex; align-items: baseline; gap: 6px;
    font-size: 18px; font-weight: 500;
  }
  .field-line { flex: 1; border-bottom: 1px solid var(--rule); }
  .field-row .field-line:first-of-type { margin-right: 4px; }

  /* ---------- Front: contact side ---------- */
  .front-brand {
    position: absolute;
    top: 52px; left: 0; right: 0;
    display: flex; justify-content: center; align-items: center; gap: 12px;
    color: var(--red);
    font-weight: 600;
    text-transform: uppercase;
    letter-spacing: 2px;
    font-size: 30px;
    line-height: 1.05;
    text-align: center;
  }
  .front-brand .brand-dot { width: 20px; height: 20px; }
  .person {
    position: absolute; top: 404px; left: 0; right: 0;
    text-align: center;
  }
  .person__name { font-size: 38px; line-height: 1.2; font-weight: 400; color: var(--charcoal); }
  .person__first { color: var(--red); font-weight: 700; }
  .person__role { font-size: 19px; font-weight: 500; margin-top: -2px; }
  .divider {
    position: absolute; left: 0; right: 0;
    display: flex; justify-content: center; align-items: center; gap: 10px;
  }
  .divider--contact { top: 497px; }
  .divider--address { top: 637px; }
  .divider__line { height: 2px; background: var(--red); }
  .divider--contact .divider__line { width: 56px; }
  .divider--address .divider__line { width: 118px; }
  .icon { width: 30px; height: 30px; display: block; }
  .contact, .address {
    position: absolute; left: 0; right: 0;
    text-align: center;
    font-size: 19.5px; font-weight: 500; line-height: 27.5px;
  }
  .contact { top: 537px; }
  .address { top: 669px; letter-spacing: .3px; }
</style>
</head>
<body>

<section class="card card--back" aria-label="Appointment side">
  <div class="back-layout">
    <div class="back-brand"><span class="brand-dot"></span><span>Bellmoor<br>Cardiology</span></div>
    <h2 class="back-title">Appointment</h2>

    <div class="slot slot--first">
      <div class="slot__days"><span>Sun</span><span>Mon</span><span>Tue</span><span>Wed</span><span>Thr</span><span>Fri</span><span>Sat</span></div>
      <div class="slot__fields">
        <div class="field-row">Date/Month <span class="field-line"></span> Year <span class="field-line"></span></div>
        <div class="field-row">Time <span class="field-line"></span></div>
      </div>
    </div>

    <div class="slot slot--second">
      <div class="slot__days"><span>Sun</span><span>Mon</span><span>Tue</span><span>Wed</span><span>Thr</span><span>Fri</span><span>Sat</span></div>
      <div class="slot__fields">
        <div class="field-row">Date/Month <span class="field-line"></span> Year <span class="field-line"></span></div>
        <div class="field-row">Time <span class="field-line"></span></div>
      </div>
    </div>
  </div>
</section>

<section class="card card--front" aria-label="Contact side">
  <div class="front-brand"><span class="brand-dot"></span><span>Bellmoor<br>Cardiology</span></div>

  <div class="person">
    <h1 class="person__name"><span class="person__first">Maren</span> Tollivar</h1>
    <p class="person__role">Founder &amp; CEO</p>
  </div>

  <div class="divider divider--contact">
    <span class="divider__line"></span>
    <svg class="icon" viewBox="0 0 30 30" aria-label="Phone"><rect x="6" y="6" width="18" height="18" rx="3" transform="rotate(45 15 15)" fill="#e8202a"/><path d="M11.5 10.5l2 -.5 1 2.5-1.3 1a6 6 0 0 0 3.3 3.3l1-1.3 2.5 1-.5 2c-4.5.3-8.3-3.5-8-8z" fill="#fff"/></svg>
    <svg class="icon" viewBox="0 0 30 30" aria-label="Email"><rect x="6" y="6" width="18" height="18" rx="3" transform="rotate(45 15 15)" fill="#e8202a"/><rect x="9.5" y="11" width="11" height="8" fill="none" stroke="#fff" stroke-width="1.3"/><path d="M9.5 11l5.5 4.5 5.5-4.5" fill="none" stroke="#fff" stroke-width="1.3"/></svg>
    <svg class="icon" viewBox="0 0 30 30" aria-label="Website"><rect x="6" y="6" width="18" height="18" rx="3" transform="rotate(45 15 15)" fill="#e8202a"/><circle cx="15" cy="15" r="5.5" fill="none" stroke="#fff" stroke-width="1.3"/><path d="M9.5 15h11M15 9.5c-2.5 3-2.5 8 0 11M15 9.5c2.5 3 2.5 8 0 11" fill="none" stroke="#fff" stroke-width="1"/></svg>
    <span class="divider__line"></span>
  </div>

  <address class="contact" style="font-style:normal">
    +001 303 555 0142<br>
    info@bellmoorheart.com<br>
    www.bellmoorheart.com
  </address>

  <div class="divider divider--address">
    <span class="divider__line"></span>
    <svg class="icon" viewBox="0 0 30 30" aria-label="Location"><rect x="6" y="6" width="18" height="18" rx="3" transform="rotate(45 15 15)" fill="#e8202a"/><path d="M15 21s-4-4.2-4-7a4 4 0 0 1 8 0c0 2.8-4 7-4 7z" fill="none" stroke="#fff" stroke-width="1.3"/><circle cx="15" cy="14" r="1.4" fill="#fff"/></svg>
    <span class="divider__line"></span>
  </div>

  <address class="address" style="font-style:normal">
    1180 Harlow Ridge Road<br>
    Ashby, CO 80612
  </address>
</section>

</body>
</html>
```